Landing Page Design for Adult Dating Age Verification (18+)

The objective of this task is to design a visually appealing pre-landing page for the adult dating site "Plumvelle (site: https://plumvelle.example/)" with an age verification mechanism. The pre-landing page will feature two buttons that redirect visitors to the main offer. The design should also include a footer block that includes links to the terms of use, privacy policy, and contact us pages.

Design Requirements:
Develop an age verification section prominently displayed on the pre-landing page.
Design the section to include two buttons labeled "Yes" and "No" for visitors to confirm their age.
Ensure the section is visually appealing and clearly communicates the purpose of age verification.

Visual Appeal:
Create a visually appealing design that aligns with the branding and theme of the "Plumvelle" adult dating site.
Use suitable color schemes, typography, and graphics to enhance the overall visual appeal of the pre-landing page.

Layout and Navigation:
Design an engaging and intuitive layout that encourages visitors to interact with the page and proceed to the main offer.
Ensure clear and visible navigation elements that direct visitors to the main offer or provide additional information.

Responsive Design:
Develop a responsive design that provides a seamless user experience across various devices, including desktop and mobile.
Ensure the design elements and layout adapt well to different screen sizes and resolutions.

File Formats and Assets:
Deliver the final design in PSD, AI, or Sketch format, ensuring that the files are well-organized and layered.
Include any necessary images or assets used in the design, ensuring they are of high quality and optimized for web use.

```html
<!DOCTYPE html>
<html lang="en">
<head>
<meta charset="utf-8">
<title>Plumvelle — Age Verification</title>
<link rel="stylesheet" href="https://fonts.googleapis.com/css2?family=DM+Serif+Display&family=Questrial&display=swap">
<style>
  :root {
    --plum-light: #9a5aa8;
    --plum-mid: #6e2c7c;
    --plum-deep: #2c0a30;
    --lilac: #d6b6dc;
    --footer-bg: #d3b4d7;
    --white: #ffffff;
  }
  * { margin: 0; padding: 0; box-sizing: border-box; }
  html, body {
    width: 1200px;
    height: 687px;
    overflow: hidden;
    background: var(--plum-deep);
  }
  .page {
    position: relative;
    width: 1200px;
    height: 687px;
    overflow: hidden;
  }
  .hero {
    position: absolute;
    left: 0; top: 0;
    width: 1200px;
    height: 624px;
  }
  .hero-photo {
    position: absolute;
    inset: 0;
    background:
      radial-gradient(ellipse at 30% 35%, rgba(190,130,200,0.55), transparent 55%),
      radial-gradient(ellipse at 80% 70%, rgba(20,0,25,0.7), transparent 60%),
      linear-gradient(100deg, var(--plum-light) 0%, var(--plum-mid) 45%, #4a1550 75%, var(--plum-deep) 100%);
  }
  .brand {
    position: absolute;
    left: 100px;
    top: 30px;
    display: flex;
    align-items: center;
    gap: 12px;
    color: var(--white);
    font-family: "DM Serif Display", serif;
    font-size: 36px;
    text-decoration: none;
  }
  .brand-dot {
    width: 40px;
    height: 40px;
    border-radius: 50%;
    background: var(--lilac);
  }
  .verify {
    position: absolute;
    left: 0;
    top: 200px;
    width: 1200px;
    text-align: center;
    color: var(--white);
  }
  .verify-title {
    font-family: "DM Serif Display", serif;
    font-weight: 400;
    font-size: 46px;
    line-height: 44px;
    letter-spacing: 0.5px;
  }
  .verify-note {
    margin-top: 35px;
    font-family: "Questrial", sans-serif;
    font-size: 17px;
    letter-spacing: 0.5px;
  }
  .verify-actions {
    margin-top: 27px;
    display: flex;
    justify-content: center;
    gap: 20px;
  }
  .btn {
    width: 160px;
    height: 44px;
    border-radius: 22px;
    display: flex;
    align-items: center;
    justify-content: center;
    font-family: "DM Serif Display", serif;
    font-size: 13px;
    color: var(--white);
    text-decoration: none;
    letter-spacing: 0.3px;
  }
  .btn-yes { background: var(--lilac); }
  .btn-no { border: 1px solid var(--lilac); }
  .footer {
    position: absolute;
    left: 0; top: 624px;
    width: 1200px;
    height: 63px;
    background: var(--footer-bg);
  }
  .footer-link {
    position: absolute;
    top: 22px;
    font-family: "DM Serif Display", serif;
    font-size: 13px;
    letter-spacing: 0.5px;
    color: var(--white);
    text-decoration: none;
    text-transform: uppercase;
  }
  .footer-privacy { left: 103px; }
  .footer-terms { left: 600px; transform: translateX(-50%); }
  .footer-contact { right: 100px; }
</style>
</head>
<body>
<div class="page">
  <section class="hero">
    <div class="hero-photo" role="img" aria-label="Photo of a masked woman in lingerie reclining on a tufted velvet sofa, tinted purple"></div>
    <a class="brand" href="https://plumvelle.example/"><span class="brand-dot"></span>Plumvelle</a>
    <div class="verify">
      <h1 class="verify-title">The site contains sexually<br>explicit material.</h1>
      <p class="verify-note">ENTER ONLY IF YOU ARE OVER 18</p>
      <div class="verify-actions">
        <a class="btn btn-yes" href="https://plumvelle.example/">I AM OVER 18</a>
        <a class="btn btn-no" href="#">I AM UNDER 18</a>
      </div>
    </div>
  </section>
  <footer class="footer">
    <a class="footer-link footer-privacy" href="#">Privacy Policy</a>
    <a class="footer-link footer-terms" href="#">Terms and Conditions</a>
    <a class="footer-link footer-contact" href="#">Contact Us</a>
  </footer>
</div>
</body>
</html>
```